Label Design for a New Alcoholized Root Beer

Create a design for a new alcoholized root beer. This is a new product category in the USA growing very rapidly. Root Beer is a popular flavor of Cola, but recently, beer manufacturers have added alcohol to it and have created a new product that has gained traction on the market at a tremendous rate.

Root Beer is vintage product that has been around for a hundred years. Consumers of this product are mostly male between the age of 30 to 45. They purchase this product for its nostalgia and vintage look and taste.

This product will be in a standard 355 mL brown bottle.

It is 5.9% abv.

The name of the product is ''Corvel's Hard Root Beer''.

We have uploaded some pictures of traditional root beers to give you an idea of the feel we want our product to have and also, the bottle the product will be filled in.

Target Market(s)

Consumers are male 30-45, same market as craft beer consumers

Industry/Entity Type

Product

Requirements
Must have
• Design must have a vintage feel to it

```html
<!DOCTYPE html>
<html lang="en">
<head>
<meta charset="utf-8">
<title>Corvel's Hard Root Beer – Bottle Label</title>
<link href="https://fonts.googleapis.com/css2?family=Rye&family=Old+Standard+TT:wght@400;700&family=Metamorphous&display=swap" rel="stylesheet">
<style>
  :root {
    --page: #ffffff;
    --paper: #e6dccd;
    --rim: #a3895d;
    --banner: #9c8459;
    --ink: #1d302e;
    --ink-light: #3f5a57;
    --cream: #efe4cc;
    --sketch: #b9a27b;
  }
  * { margin: 0; padding: 0; box-sizing: border-box; }
  html, body {
    width: 876px; height: 1200px; overflow: hidden;
    background: var(--page);
  }
  .label { position: relative; width: 876px; height: 1200px; overflow: hidden; }
  .label-shape { position: absolute; inset: 0; }

  .brand-banner { position: absolute; left: 172px; top: 160px; width: 530px; height: 195px; }
  .brand-name {
    position: absolute; left: 172px; top: 172px; width: 530px;
    text-align: center;
    font-family: "Metamorphous", serif;
    font-size: 84px; line-height: 1; letter-spacing: 1px;
    color: var(--ink);
    transform: scaleY(1.5); transform-origin: top center;
  }
  .brand-est {
    position: absolute; left: 172px; top: 288px; width: 530px;
    text-align: center;
    font-family: "Old Standard TT", serif;
    font-size: 24px; line-height: 1; color: var(--cream);
  }
  .brand-est .dot {
    display: inline-block; width: 8px; height: 8px; border-radius: 50%;
    background: var(--ink); vertical-align: middle; margin: 0 5px;
  }

  .hand-art {
    position: absolute; left: 76px; top: 376px; width: 372px; height: 222px;
    border-radius: 48% 30% 40% 50% / 50% 30% 60% 50%;
    background: radial-gradient(ellipse at 40% 55%, #d4c4a6 0%, #ddd0b8 60%, rgba(230,220,205,0) 100%);
  }
  .flag { position: absolute; left: 430px; top: 400px; width: 225px; height: 155px; }
  .flag-word {
    position: absolute; left: 470px; top: 462px; width: 170px;
    font-family: "Metamorphous", serif; font-size: 44px; line-height: 1;
    color: var(--cream);
  }
  .flag-abv {
    position: absolute; left: 472px; top: 510px; width: 170px;
    font-family: "Old Standard TT", serif; font-size: 19px; line-height: 1;
    color: var(--cream);
  }

  .hops-art {
    position: absolute; left: 235px; top: 580px; width: 430px; height: 450px;
    border-radius: 45%;
    background: radial-gradient(ellipse at center, rgba(190,172,140,0.45) 0%, rgba(200,184,156,0.25) 55%, rgba(230,220,205,0) 75%);
  }

  .title-block {
    position: absolute; left: 450px; top: 790px;
    width: 0; height: 0;
    transform: rotate(-26deg);
  }
  .title-word {
    position: absolute; width: 700px;
    text-align: center;
    font-family: "Rye", serif;
    font-size: 172px; line-height: 1; letter-spacing: 6px;
    color: var(--ink);
    text-shadow: 2px 3px 0 var(--ink-light), 5px 7px 6px rgba(0,0,0,0.35);
  }
  .title-word.root { top: -178px; left: -360px; }
  .title-word.beer { top: 6px; left: -340px; }
  .title-rule {
    position: absolute; left: -327px; top: -2px;
    width: 654px; height: 4px; background: var(--ink);
  }
  .title-rule::before, .title-rule::after {
    content: ""; position: absolute; top: -5px;
    width: 13px; height: 13px; border-radius: 50%; background: var(--ink);
  }
  .title-rule::before { left: -6px; }
  .title-rule::after { right: -6px; }

  .volume {
    position: absolute; left: 0; top: 1128px; width: 876px;
    text-align: center;
    font-family: "Old Standard TT", serif; font-size: 20px; line-height: 1;
    color: var(--ink);
  }
</style>
</head>
<body>
<main class="label">
  <svg class="label-shape" viewBox="0 0 876 1200" aria-hidden="true">
    <defs>
      <radialGradient id="paperTone" cx="50%" cy="45%" r="60%">
        <stop offset="0%" stop-color="#e9e0d2"/>
        <stop offset="100%" stop-color="#ddd1bd"/>
      </radialGradient>
    </defs>
    <ellipse cx="438" cy="600" rx="404" ry="582" fill="url(#paperTone)" stroke="var(--rim)" stroke-width="9"/>
  </svg>

  <svg class="brand-banner" viewBox="0 0 530 195" aria-hidden="true">
    <path d="M10 20 Q140 2 265 14 Q395 28 520 8 L506 90 L524 178 Q395 195 265 182 Q140 170 10 188 L26 100 Z" fill="var(--banner)"/>
  </svg>
  <div class="brand-name">CORVEL'S</div>
  <div class="brand-est"><span class="dot"></span>est. 2016<span class="dot"></span></div>

  <div class="hand-art" role="img" aria-label="Vintage engraved hand pointing to the right"></div>

  <svg class="flag" viewBox="0 0 225 155" aria-hidden="true">
    <line x1="0" y1="22" x2="20" y2="22" stroke="var(--sketch)" stroke-width="4"/>
    <line x1="20" y1="12" x2="20" y2="145" stroke="var(--sketch)" stroke-width="4"/>
    <path d="M22 26 Q120 12 220 28 L212 140 Q120 126 22 136 Z" fill="var(--banner)"/>
  </svg>
  <div class="flag-word">HARD</div>
  <div class="flag-abv">5.9%abv</div>

  <div class="hops-art" role="img" aria-label="Faint sketch of hops, leaves and roots"></div>

  <div class="title-block">
    <div class="title-word root">ROOT</div>
    <div class="title-rule"></div>
    <div class="title-word beer">BEER</div>
  </div>

  <div class="volume">8 fl. oz.</div>
</main>
</body>
</html>
```